The logo name is "Harbon Vellis". The name of the product will be "Tavoren Calm". This product is specifically formulated for amputees. Therefore under the product name it should state "for amputees". The catch phrase will be "Experience Harbon gain Wellstride"
These are the things we need on the label:
Logo, product name, "for amputees", "Experience Harbon gain Wellstride", Safe, Effective, Directions: spray on problem areas, no need to dry off. harbonvellis.example, Made in Canada, 500ml.
The MOST IMPORTANT and therefore the most prominent thing on this lable will be the LOGO! The second most prominent thing will be the word "Calm" We want to keep it very plain, very simple, very unclutered. Keep in mind that this lable will be placed on a white bottle or have a white back ground. The 500ml white PE bottle with trigger sprayer will have a tear drop label. See attached die line (S-294).
We want to stay with the colours that goes with the colour scheme of the logo. See attached logo. Soft colours. We do not want a picture! We would like the lable to be classy and rich.
Updates
The logo name is "Harbon Vellis". The name of the product will be "Tavoren Calm". This product is specificlly formulated for amputees. Therefore under the product name it should state "for amputees". The catch phrase will be "Experience Harbon gain Wellstride"
Logo, product name, "for amputees", catch phrase "Experience Harbon gain Wellstride", Clean, Safe, Effective, Directions: spray on problem areas, no need to dry off. Also Harbon Vellis Corpation, harbonvellis.example, Made in Canada, 500ml.
We want to stay with the colour scheme of the logo. See attached logo. Soft colours. We do not want a picture! We would like the lable to be classy and rich.
This is the offical directive that came from the governing panal of this lable. This panal it not know where it wanted to take this lable that would represent this line until they review all of your submissions, thank you for all your talented hard work. But now it is clear it is time to regroup and hit this objective.
Target Market(s)
Amputees and Parents of.
Industry/Entity Type
Product
Requirements
Must have
- Final product to be in a pdf or an illustrator file

```html
<!DOCTYPE html>
<html lang="en">
<head>
<meta charset="utf-8">
<title>Harbon Vellis – Tavoren Calm Conditioner Label</title>
<link rel="stylesheet" href="https://fonts.googleapis.com/css2?family=Archivo+Black&family=PT+Sans:wght@400;700&family=PT+Sans+Narrow:wght@400;700&display=swap">
<style>
  :root {
    --page: #ffffff;
    --orange-light: #ffa21f;
    --orange: #f07a12;
    --red: #c8261a;
    --cream: #fff7d6;
    --yellow: #ffd21a;
    --olive: #8a7a2a;
    --plum: #7b1466;
    --plum-text: #6a1658;
    --pill-red: #c01e1e;
    --logo-green: #1f4a2e;
    --logo-teal: #2f9e8f;
    --white: #ffffff;
    --caption: #111111;
  }
  html, body {
    margin: 0;
    padding: 0;
    width: 1200px;
    height: 900px;
    overflow: hidden;
    background: var(--page);
  }
  .canvas {
    position: relative;
    width: 1200px;
    height: 900px;
  }
  .artwork {
    position: absolute;
    inset: 0;
  }
  .headline {
    font-family: "Archivo Black", "Arial Black", sans-serif;
    fill: var(--plum);
    stroke: var(--white);
    paint-order: stroke;
    stroke-linejoin: round;
  }
  .pill-text {
    font-family: "Archivo Black", "Arial Black", sans-serif;
    fill: var(--white);
  }
  .brand-name {
    font-family: "PT Sans Narrow", "Arial Narrow", sans-serif;
    font-weight: 700;
    fill: var(--logo-green);
  }
  .band-text {
    font-family: "PT Sans Narrow", "Arial Narrow", sans-serif;
    fill: var(--white);
  }
  .view-caption {
    font-family: "PT Sans", Arial, sans-serif;
    font-weight: 700;
    font-size: 15px;
    fill: var(--caption);
  }
  .body-column {
    position: absolute;
    font-family: "PT Sans", Arial, sans-serif;
    font-size: 7.6px;
    line-height: 9.6px;
    color: var(--plum-text);
    text-align: justify;
  }
  .body-column p { margin: 0 0 9px; }
  .body-column--left { left: 668px; top: 392px; width: 148px; }
  .body-column--right { left: 826px; top: 338px; width: 172px; }
</style>
</head>
<body>
<div class="canvas">
  <svg class="artwork" width="1200" height="900" viewBox="0 0 1200 900" xmlns="http://www.w3.org/2000/svg">
    <defs>
      <linearGradient id="shell" x1="0" y1="0" x2="1" y2="0">
        <stop offset="0" stop-color="var(--red)"/>
        <stop offset="0.35" stop-color="var(--orange)"/>
        <stop offset="0.6" stop-color="var(--orange-light)"/>
        <stop offset="1" stop-color="var(--red)"/>
      </linearGradient>
      <radialGradient id="panel" cx="0.45" cy="0.5" r="0.65">
        <stop offset="0" stop-color="var(--cream)"/>
        <stop offset="0.55" stop-color="#fff0b0"/>
        <stop offset="1" stop-color="var(--yellow)"/>
      </radialGradient>
      <clipPath id="front-die">
        <path d="M440,90 C472,92 490,200 522,320 C560,450 575,610 515,738 L225,738 C172,640 180,520 225,405 C285,255 400,108 440,90 Z"/>
      </clipPath>
      <clipPath id="back-die">
        <path d="M752,90 C792,100 880,200 958,320 C1032,445 1045,620 990,738 L690,738 C640,620 640,470 678,330 C710,205 728,102 752,90 Z"/>
      </clipPath>
    </defs>

    <!-- Front label -->
    <g class="label label--front" clip-path="url(#front-die)">
      <rect x="170" y="80" width="420" height="670" fill="url(#shell)"/>
      <path d="M170,330 C300,250 410,195 590,225 L590,585 C440,580 320,600 170,500 Z" fill="url(#panel)"/>
      <path d="M170,330 C300,250 410,195 590,225" fill="none" stroke="var(--olive)" stroke-width="7"/>
      <path d="M170,500 C320,600 440,580 590,580 L590,610 C470,650 400,700 330,690 C260,680 210,650 170,610 Z" fill="var(--plum)"/>
    </g>
    <g class="front-content">
      <rect x="268" y="325" width="50" height="50" fill="var(--logo-teal)"/>
      <text class="brand-name" x="328" y="364" font-size="36">Harbon Vellis</text>
      <g transform="rotate(-10 365 470)">
        <text class="headline" x="368" y="463" font-size="40" stroke-width="5" text-anchor="middle">Tavoren Calm</text>
        <text class="headline" x="370" y="506" font-size="35" stroke-width="5" text-anchor="middle">Conditioner</text>
        <rect x="258" y="525" width="240" height="40" rx="8" fill="var(--pill-red)"/>
        <text class="pill-text" x="378" y="554" font-size="25" text-anchor="middle">For Amputees</text>
      </g>
      <text class="band-text" x="378" y="649" font-size="25" text-anchor="middle">Naturally Hygienic</text>
      <text class="band-text" x="370" y="716" font-size="22" text-anchor="middle">500mL</text>
    </g>

    <!-- Back label -->
    <g class="label label--back" clip-path="url(#back-die)">
      <rect x="630" y="80" width="420" height="670" fill="url(#shell)"/>
      <path d="M630,260 C690,230 740,200 800,210 C880,225 960,300 1050,420 L1050,565 C900,572 760,582 630,585 Z" fill="url(#panel)"/>
      <path d="M630,260 C690,230 740,200 800,210 C880,225 960,300 1050,420" fill="none" stroke="var(--olive)" stroke-width="6"/>
      <path d="M630,585 C760,582 900,572 1050,565 L1050,615 C960,640 900,662 830,664 C760,664 700,640 630,622 Z" fill="var(--plum)"/>
    </g>
    <g class="back-content">
      <rect x="700" y="254" width="20" height="20" fill="var(--logo-teal)"/>
      <text class="brand-name" x="726" y="271" font-size="18">Harbon Vellis</text>
      <g transform="rotate(-10 745 325)">
        <text class="headline" x="746" y="318" font-size="20" stroke-width="3" text-anchor="middle">Tavoren Calm</text>
        <text class="headline" x="748" y="340" font-size="18" stroke-width="3" text-anchor="middle">Conditioner</text>
        <rect x="692" y="349" width="118" height="21" rx="5" fill="var(--pill-red)"/>
        <text class="pill-text" x="751" y="365" font-size="13" text-anchor="middle">For Amputees</text>
      </g>
      <text class="band-text" x="828" y="651" font-size="18" text-anchor="middle">Naturally Hygienic</text>
      <text class="band-text" x="835" y="716" font-size="19" text-anchor="middle">500mL</text>
    </g>

    <text class="view-caption" x="369" y="779" text-anchor="middle">Front</text>
    <text class="view-caption" x="833" y="779" text-anchor="middle">Back</text>
  </svg>

  <div class="body-column body-column--left">
    <p>Tavoren Calm is a gentle conditioner made for the skin of the residual limb. It helps keep skin clean, soft and comfortable under a liner or socket through the whole day. The light formula leaves no sticky feel and suits daily use at home or on the go. Directions: spray on problem areas, no need to dry off. Use after washing and before putting on your liner. Repeat as needed.</p>
    <p>Safe and effective for adults and children. For external use only. Avoid contact with eyes. If irritation occurs, stop use and ask your care provider. Keep out of reach of young children.</p>
  </div>
  <div class="body-column body-column--right">
    <p>Clean. Safe. Effective. Experience Harbon gain Wellstride. Our care line is made with people who live with limb loss, and with the parents who care for them. Each formula is tested to be kind to skin that works hard every day.</p>
    <p>Store at room temperature and away from direct sunlight. Close the trigger after each use. Harbon Vellis Corpation, harbonvellis.example. Made in Canada. Ingredients and full safety details are listed on our website. Questions or comments are always welcome, so please reach out to our care team any time.</p>
  </div>
</div>
</body>
</html>
```